I'm an electrician and the name of my company is called Brisk 'N' Bright Electrical. I require a professional business card that speaks to my clients, I also need it to be innovative and modern. We do maintenance & service work for domestic and commercial premises.

Industry/Entity Type

Electrical

Contact Information for Business Card

Must have the name of my company Brisk 'N' Bright Electrical, my name Darren Kolovos and my contact details 0427 381 592 and company email address Brisknbrightelectrical@mailvane.com and/or website Brisknbrightelectrical.com.au

Logo Text

Brisk 'N' Bright Electrical (If possible)

Colors
33a6d7
0592cd
3176b5

```html
<!DOCTYPE html>
<html lang="en">
<head>
<meta charset="utf-8">
<title>Brisk 'N' Bright Electrical – Business Card</title>
<link rel="stylesheet" href="https://fonts.googleapis.com/css2?family=Open+Sans:wght@400;600;700&display=swap">
<style>
  :root {
    --backdrop: #d2d3d5;
    --card: #ffffff;
    --card-edge: #d9d9db;
    --ink-strong: #333538;
    --ink-soft: #606266;
    --ink-caps: #55575b;
    --accent: #0592cd;
    --accent-deep: #3176b5;
    --divider: #9a9b9e;
    --ghost-letter: #f1f1f3;
  }
  html, body {
    margin: 0;
    padding: 0;
    width: 1200px;
    height: 1145px;
    overflow: hidden;
    background: var(--backdrop);
    font-family: "Open Sans", Arial, sans-serif;
  }
  .business-card {
    position: absolute;
    left: 287px;
    top: 303px;
    width: 640px;
    height: 369px;
    background: var(--card);
    border: 1px solid var(--card-edge);
    box-sizing: border-box;
    overflow: hidden;
  }
  .ghost-letter {
    position: absolute;
    left: 66px;
    top: 72px;
    width: 118px;
    height: 210px;
  }
  .brand-mark {
    position: absolute;
    left: 50px;
    top: 158px;
    width: 150px;
    text-align: center;
    font-size: 17px;
    font-weight: 700;
    line-height: 26px;
    color: var(--ink-strong);
    white-space: nowrap;
  }
  .divider {
    position: absolute;
    left: 251px;
    top: 40px;
    width: 2px;
    height: 291px;
    background: var(--divider);
  }
  .company-name {
    position: absolute;
    left: 284px;
    top: 80px;
    margin: 0;
    font-size: 27px;
    line-height: 36px;
    font-weight: 600;
    color: var(--ink-strong);
    letter-spacing: 0.5px;
  }
  .company-tagline {
    position: absolute;
    left: 285px;
    top: 124px;
    margin: 0;
    font-size: 14px;
    line-height: 18px;
    font-weight: 600;
    color: var(--ink-caps);
    letter-spacing: 2.4px;
    text-transform: uppercase;
  }
  .person-name {
    position: absolute;
    left: 285px;
    top: 152px;
    margin: 0;
    font-size: 15px;
    line-height: 20px;
    font-weight: 600;
    color: var(--accent-deep);
  }
  .contact-list {
    position: absolute;
    left: 284px;
    top: 188px;
    margin: 0;
    padding: 0;
    list-style: none;
  }
  .contact-item {
    display: flex;
    align-items: center;
    height: 26px;
    font-size: 16px;
    color: var(--ink-soft);
    white-space: nowrap;
  }
  .contact-icon {
    width: 14px;
    height: 14px;
    margin-right: 14px;
    flex: none;
  }
</style>
</head>
<body>
  <section class="business-card">
    <svg class="ghost-letter" viewBox="0 0 118 210" aria-hidden="true">
      <polygon points="0,0 34,0 86,138 86,0 118,0 118,210 86,210 32,70 32,210 0,210" fill="var(--ghost-letter)"/>
    </svg>
    <div class="brand-mark">Brisk 'N' Bright</div>
    <div class="divider"></div>

    <h1 class="company-name">Brisk 'N'</h1>
    <p class="company-tagline">Bright Electrical</p>
    <p class="person-name">Darren Kolovos</p>

    <ul class="contact-list">
      <li class="contact-item">
        <svg class="contact-icon" viewBox="0 0 14 14" aria-hidden="true">
          <rect x="3.5" y="1" width="7" height="12" rx="1.2" fill="none" stroke="var(--accent)" stroke-width="1.8"/>
          <rect x="6" y="10.2" width="2" height="1.2" fill="var(--accent)"/>
        </svg>
        0427 381 592
      </li>
      <li class="contact-item">
        <svg class="contact-icon" viewBox="0 0 14 14" aria-hidden="true">
          <circle cx="7" cy="7" r="5.5" fill="var(--accent)"/>
          <ellipse cx="7" cy="7" rx="2.4" ry="5.5" fill="none" stroke="#ffffff" stroke-width="0.8"/>
          <line x1="1.5" y1="7" x2="12.5" y2="7" stroke="#ffffff" stroke-width="0.8"/>
        </svg>
        Brisknbrightelectrical.com.au
      </li>
      <li class="contact-item">
        <svg class="contact-icon" viewBox="0 0 14 14" aria-hidden="true">
          <rect x="1" y="3" width="12" height="8" rx="1" fill="var(--accent)"/>
          <path d="M1.5 3.6 L7 7.6 L12.5 3.6" fill="none" stroke="#ffffff" stroke-width="0.8"/>
        </svg>
        Brisknbrightelectrical@mailvane.com
      </li>
    </ul>
  </section>
</body>
</html>
```